BLUE FORGE (Business Card for Training Company)

Blue Forge is a training and consultancy company with a focus on executive protection and medical. I would like the card to be nice and sharp, not overdone and in black and red. I would also like it to highlight that it is "A Tavmont Company"

I would like it to be simple and highlight a few things.

1. Name
2. Title
3. Phone Number
4. Email

I would also like www.tavmontgroup.example/blue-forge to be on the card somewhere.

Target Market(s)

Security Companies

Industry/Entity Type

Security

Contact Information for Business Card

Blue Forge is a training and consultancy company with a focus on executive protection and medical. I would like the card to be nice and sharp, not overdone and in black and red. I would also like it to highlight that it is "A Tavmont Company" I would like it to be simple and highlight a few things. 1. Name 2. Title 3. Phone Number 4. Email I would also like www.tavmontgroup.example/blue-forge to be on the card somewhere.

Requirements
Must have
• A Tavmont Company listed on the card and the website
Nice to have
• Highlight Medical Training, Consultancy & Executive Protection Courses

```html
<!DOCTYPE html>
<html lang="en">
<head>
<meta charset="utf-8">
<title>Blue Forge – Business Card</title>
<link href="https://fonts.googleapis.com/css2?family=Archivo:wght@400;700;900&display=swap" rel="stylesheet">
<style>
  :root {
    --stage: #dcdcdc;
    --black: #0c0c0c;
    --red: #6e0e12;
    --red-light: #8a1a1e;
    --white: #ffffff;
    --ghost: #2a2a2a;
  }
  html, body {
    margin: 0;
    width: 1200px;
    height: 900px;
    overflow: hidden;
    background: var(--stage);
    font-family: "Archivo", Arial, sans-serif;
  }
  .stage {
    width: 1200px;
    height: 900px;
    display: flex;
    flex-direction: column;
    align-items: center;
    justify-content: center;
    gap: 44px;
  }
  .card {
    width: 720px;
    height: 380px;
    display: block;
    box-shadow: 0 6px 14px rgba(0,0,0,0.25);
  }
  .brand-name { font-family: "Archivo", Arial, sans-serif; font-weight: 900; fill: var(--red); }
  .brand-name-front { font-family: "Archivo", Arial, sans-serif; font-weight: 900; fill: var(--white); font-size: 64px; }
  .tagline { font-family: "Archivo", Arial, sans-serif; font-weight: 900; fill: var(--white); font-size: 22px; letter-spacing: 0.5px; }
  .parent-company { font-family: "Archivo", Arial, sans-serif; font-weight: 900; fill: var(--white); font-size: 22px; letter-spacing: 1px; }
  .person-name { font-family: "Archivo", Arial, sans-serif; font-weight: 700; fill: var(--white); font-size: 26px; }
  .person-title { font-family: "Archivo", Arial, sans-serif; font-weight: 400; fill: var(--white); font-size: 16px; }
  .contact-line { font-family: "Archivo", Arial, sans-serif; font-weight: 400; fill: var(--white); font-size: 19px; }
  .watermark { font-family: "Archivo", Arial, sans-serif; font-weight: 900; fill: var(--ghost); font-size: 60px; }
  .icon { fill: var(--red-light); }
</style>
</head>
<body>
<main class="stage">

  <!-- Front of card -->
  <svg class="card card-front" viewBox="0 0 720 380" aria-label="Blue Forge card front">
    <rect width="720" height="380" fill="var(--black)"/>
    <rect class="red-band" x="0" y="150" width="720" height="194" fill="var(--red)"/>
    <text class="brand-name-front" x="60" y="116">BLUE FORGE</text>
    <text class="tagline" x="430" y="250" text-anchor="middle">MEDICAL TRAINING, CONSULTANCY &amp;</text>
    <text class="tagline" x="430" y="284" text-anchor="middle">EXECUTIVE PROTECTION COURSES</text>
  </svg>

  <!-- Back of card -->
  <svg class="card card-back" viewBox="0 0 720 380" aria-label="Blue Forge card back">
    <defs>
      <clipPath id="card-clip"><rect width="720" height="380"/></clipPath>
    </defs>
    <g clip-path="url(#card-clip)">
      <rect width="720" height="380" fill="var(--white)"/>
      <text class="brand-name" x="36" y="92" font-size="62">BLUE</text>
      <text class="brand-name" x="36" y="156" font-size="62">FORGE</text>

      <rect class="rule" x="30" y="196" width="440" height="4" fill="var(--black)"/>
      <rect class="parent-band" x="30" y="206" width="440" height="44" fill="var(--red)"/>
      <text class="parent-company" x="52" y="236">A TAVMONT COMPANY</text>

      <path class="dark-field" d="M0 260 H470 V178 H720 V352 H0 Z" fill="var(--black)"/>
      <rect class="bottom-strip" x="0" y="352" width="720" height="28" fill="var(--red)"/>

      <path class="name-tab" d="M474 170 Q474 152 492 150 L650 140 Q700 140 720 152 V206 L500 224 Q474 224 474 206 Z" fill="var(--red-light)"/>
      <text class="person-name" x="700" y="182" text-anchor="end">Dana Okoro</text>
      <text class="person-title" x="700" y="202" text-anchor="end">Manager</text>

      <text class="watermark" x="480" y="290">BLUE</text>
      <text class="watermark" x="480" y="344">FORGE</text>

      <!-- phone -->
      <path class="icon" d="M62 282 h14 l3 6 h-20 z M60 289 h22 v6 h-22 z"/>
      <text class="contact-line" x="100" y="294">012 555 0147</text>
      <!-- email -->
      <path class="icon" d="M60 308 h22 v14 h-22 z"/>
      <path d="M60 308 l11 8 l11 -8" fill="none" stroke="var(--black)" stroke-width="1.5"/>
      <text class="contact-line" x="100" y="321">info@tavmontgroup.example</text>
      <!-- web -->
      <circle class="icon" cx="71" cy="341" r="8"/>
      <text class="contact-line" x="100" y="347">www.tavmontgroup.example/blue-forge</text>
    </g>
  </svg>

</main>
</body>
</html>
```